Pediatric Occupational Therapy Brochure Design

This design really needs to stand out, especially with all the wordage that I have included. These brochures will be given to doctors, future clients, and caregivers. I have included the logo on by brochure, so incorporating the same or similar colors would be fantastic. A trifold brochure would probably be best to fit all the information, as this is a new business and needs to convey all the information in a way that people will read.

Target Market(s)

Doctor's offices and caregivers of children with disabilities.

Industry/Entity Type

Health Care

Font styles to use
Serif
Sans Serif

Colors
33a6d7
85acd3
ffffff
33b8a4
86cfc7

Requirements
Must have
• I would like the same colors of the logo incorporated in the brochure design.
Nice to have
• I would like to see the butterfly somehow in the background or used in the design. Also a trifold or two page design would be greatly appreciated as long as the information can fit.

```html
<!DOCTYPE html>
<html lang="en">
<head>
<meta charset="UTF-8">
<title>Lark &amp; Fern Therapy – Brochure Cover</title>
<link rel="stylesheet" href="https://fonts.googleapis.com/css2?family=Open+Sans:wght@400;600;700&display=swap">
<style>
  :root {
    --canvas: #efefef;
    --paper: #ffffff;
    --paper-edge: #e4e4e4;
    --teal: #33b8a4;
    --teal-deep: #1fa593;
    --teal-soft: #86cfc7;
    --sky: #33a6d7;
    --ink: #555555;
    --ink-dark: #3a3a3a;
  }
  * { box-sizing: border-box; margin: 0; padding: 0; }
  html, body {
    width: 1200px;
    height: 1000px;
    overflow: hidden;
    background: var(--canvas);
    font-family: "Open Sans", Arial, sans-serif;
  }
  .cover-panel {
    position: absolute;
    left: 400px;
    top: 50px;
    width: 400px;
    height: 900px;
    background: var(--paper);
    box-shadow: 0 2px 12px rgba(0,0,0,0.08);
    overflow: hidden;
  }
  .brand {
    position: absolute;
    top: 120px;
    left: 0;
    width: 100%;
    display: flex;
    align-items: center;
    justify-content: center;
    gap: 22px;
  }
  .brand-name {
    font-size: 30px;
    font-weight: 400;
    color: var(--ink);
    letter-spacing: 2px;
    line-height: 1.15;
    text-align: center;
  }
  .brand-mark {
    width: 46px;
    height: 46px;
    border-radius: 50%;
    background: var(--teal-soft);
  }
  .cover-art {
    position: absolute;
    left: 0;
    top: 0;
    width: 400px;
    height: 900px;
  }
  .service-title {
    position: absolute;
    left: 80px;
    top: 660px;
    width: 320px;
    text-align: center;
    color: var(--paper);
    font-weight: 600;
    font-size: 24px;
    line-height: 1.25;
  }
  .service-title .service-note {
    display: block;
    font-size: 18px;
    font-weight: 600;
  }
  .web-address {
    position: absolute;
    left: 0;
    top: 818px;
    width: 100%;
    text-align: center;
    font-size: 18px;
    font-weight: 700;
    color: var(--ink-dark);
  }
</style>
</head>
<body>
  <main class="cover-panel">
    <svg class="cover-art" viewBox="0 0 400 900" xmlns="http://www.w3.org/2000/svg">
      <defs>
        <linearGradient id="photoTones" x1="0" y1="0" x2="1" y2="1">
          <stop offset="0" stop-color="#7cc24a"/>
          <stop offset="0.3" stop-color="#d9b79a"/>
          <stop offset="0.55" stop-color="#2f9fd8"/>
          <stop offset="0.8" stop-color="#f2c230"/>
          <stop offset="1" stop-color="#d9332f"/>
        </linearGradient>
        <linearGradient id="bandTeal" x1="0" y1="0" x2="1" y2="0">
          <stop offset="0" stop-color="var(--teal-deep)"/>
          <stop offset="1" stop-color="var(--teal)"/>
        </linearGradient>
      </defs>
      <path class="photo-area" role="img" aria-label="Photo of smiling children lying in a circle, making goggles with their hands"
            fill="url(#photoTones)"
            d="M0 300 L400 245 L400 575 C300 600 180 620 0 650 Z"/>
      <path class="wave-band" fill="url(#bandTeal)"
            d="M0 650 C180 620 300 600 400 575 L400 598 C300 625 160 660 0 690 Z"/>
      <path class="service-pill" fill="var(--teal-soft)"
            d="M110 640 L400 610 L400 770 L110 790 A75 75 0 0 1 110 640 Z"/>
    </svg>

    <div class="brand">
      <div class="brand-name">LARK &amp; FERN<br>THERAPY</div>
      <div class="brand-mark"></div>
    </div>

    <h1 class="service-title">
      Pediatric Occupational Therapy Services
      <span class="service-note">(In home services)</span>
    </h1>

    <p class="web-address">www.larkferntherapy.com</p>
  </main>
</body>
</html>
```